Tenbrook Business Card Design

We are the largest used car company fro JapanJust need a simple business cards to start with

Industry/Entity Type

Used Car

Contact Information for Business Card

Haruna " Ned" Morikawa
Operations Director
Tenbrook Australia Pty.Ltd.
P.O.Box 517 Pendlestone NSW 2093
M: 0466 518 274
P: 1800 574 392
email : haruna.morikawa@tnbk.co.jp

```html
<!DOCTYPE html>
<html lang="en">
<head>
<meta charset="utf-8">
<title>Tenbrook Business Card – Haruna Morikawa</title>
<link rel="stylesheet" href="https://fonts.googleapis.com/css2?family=Arimo:wght@400;700&display=swap">
<style>
  :root {
    --card-bg: #141414;
    --dash-fill: #1a1c1f;
    --dash-edge: #25282c;
    --dial-well: #15181d;
    --gauge-face: #e9e9e9;
    --gauge-rim: #bdbdbd;
    --name-blue: #3b7fe6;
    --text-white: #ffffff;
  }
  * { margin: 0; padding: 0; box-sizing: border-box; }
  html, body {
    width: 1200px; height: 727px; overflow: hidden;
    background: var(--card-bg);
  }
  .card {
    position: relative;
    width: 1200px; height: 727px;
    background: var(--card-bg);
    font-family: "Arimo", Arial, sans-serif;
    color: var(--text-white);
    overflow: hidden;
  }
  .dashboard { position: absolute; inset: 0; }
  .holder-name {
    position: absolute; top: 122px; left: 0; width: 1200px;
    text-align: center;
    font-size: 40px; font-weight: 700; letter-spacing: -0.6px;
    color: var(--name-blue);
  }
  .holder-title {
    position: absolute; top: 186px; left: 0; width: 1200px;
    text-align: center;
    font-size: 24px; letter-spacing: -0.5px;
  }
  .gauge {
    position: absolute; border-radius: 50%;
    background: radial-gradient(circle at 50% 45%, #ffffff 0%, var(--gauge-face) 65%, var(--gauge-rim) 100%);
  }
  .gauge-fuel { left: 534px; top: 255px; width: 130px; height: 130px; }
  .gauge-temp { left: 534px; top: 412px; width: 132px; height: 132px; }
  .company-address {
    position: absolute; left: 84px; top: 392px; width: 300px;
    text-align: center;
    font-size: 24px; line-height: 45px; letter-spacing: -0.9px;
  }
  .contact-list {
    position: absolute; left: 810px; top: 380px; width: 330px;
    font-size: 24px; letter-spacing: -0.5px;
  }
  .contact-line {
    display: flex; align-items: center; justify-content: center;
    height: 45px; gap: 12px;
  }
  .contact-line svg { flex: none; }
</style>
</head>
<body>
<div class="card">
  <svg class="dashboard" width="1200" height="727" viewBox="0 0 1200 727" aria-hidden="true">
    <path d="M0 250 C 60 120, 250 60, 420 48 L 780 48 C 950 60, 1140 120, 1200 250 L 1200 560 C 1150 690, 1000 720, 860 700 C 720 690, 680 660, 600 660 C 520 660, 480 690, 340 700 C 200 720, 50 690, 0 560 Z"
          fill="var(--dash-fill)" stroke="var(--dash-edge)" stroke-width="2"/>
    <circle cx="228" cy="430" r="190" fill="var(--dial-well)"/>
    <circle cx="967" cy="428" r="184" fill="var(--dial-well)"/>
  </svg>

  <h1 class="holder-name">Haruna “Ned” Morikawa</h1>
  <p class="holder-title">Operations Director</p>

  <div class="gauge gauge-fuel" role="img" aria-label="Fuel gauge dial with needle near empty"></div>
  <div class="gauge gauge-temp" role="img" aria-label="Engine temperature gauge dial with needle near cold"></div>

  <address class="company-address" style="font-style:normal">
    Tenbrook Australia Pty.Ltd.<br>
    P.O.Box 517 Pendlestone,<br>
    NSW 2093
  </address>

  <div class="contact-list">
    <div class="contact-line">
      <svg width="16" height="24" viewBox="0 0 16 24" aria-hidden="true">
        <rect x="1.5" y="1.5" width="13" height="21" rx="2" fill="none" stroke="#fff" stroke-width="2.2"/>
        <rect x="6" y="18" width="4" height="2" fill="#fff"/>
      </svg>
      <span>0466 518 274</span>
    </div>
    <div class="contact-line">
      <svg width="22" height="18" viewBox="0 0 22 18" aria-hidden="true">
        <path d="M1 6 C 4 1, 18 1, 21 6 L 17 8 L 15 5 L 7 5 L 5 8 Z" fill="#fff"/>
        <path d="M5 9 L 17 9 L 19 17 L 3 17 Z" fill="#fff"/>
        <circle cx="11" cy="13" r="2" fill="var(--dial-well)"/>
      </svg>
      <span>1800 574 392</span>
    </div>
    <div class="contact-line">
      <span>haruna.morikawa@tnbk.co.jp</span>
    </div>
  </div>
</div>
</body>
</html>
```